Brexalinth Web Design

We would like to have our website designed and coded. It will be a display only website - no input or output functionality. It's a fairly simple structure with not many pages, but we would like some professional design and creative elements added in to make the site attractive and sharp. I have attached a presentation with the page and content layout. Where images are included in the presentation, those are concepts that you can reorganize or layout in any way that you think looks best. Same with the wheel of services on the incubator page, and the bullet points listed on the accelerator page.

```html
<!DOCTYPE html>
<html lang="en">
<head>
<meta charset="utf-8">
<title>Brexalinth</title>
<link href="https://fonts.googleapis.com/css2?family=Mulish:wght@300;400;600&family=Raleway:wght@400;500;700;800&display=swap" rel="stylesheet">
<style>
:root{
  --brand:#1b5a80;
  --accent:#1ea7ee;
  --ink:#1a1a1a;
  --muted:#666;
  --white:#fff;
  --night:#0d151c;
  --footer:#020406;
}
*{margin:0;padding:0;box-sizing:border-box}
html,body{width:692px;height:1200px;overflow:hidden;background:var(--white)}
body{position:relative;font-family:"Mulish",sans-serif;color:var(--ink)}
.abs{position:absolute}
.site-header{position:absolute;left:0;top:0;width:692px;height:27px;background:var(--white)}
.brand{font-family:"Mulish",sans-serif;font-weight:600;letter-spacing:.5px}
.header-brand{left:41px;top:7px;font-size:11px;color:var(--brand)}
.main-nav a{position:absolute;top:10px;font-size:7px;color:var(--ink);text-decoration:none}
.hero{position:absolute;left:0;top:27px;width:692px;height:297px;
  background:linear-gradient(180deg,#3d3d3d 0%,#2b2b2b 45%,#4a4846 100%)}
.hero-brand{left:41px;top:128px;font-size:38px;color:var(--white);letter-spacing:2px}
.hero-ring{left:362px;top:4px;width:290px;height:290px;border-radius:50%;background:var(--white)}
.hero-photo{left:371px;top:13px;width:272px;height:272px;border-radius:50%;
  background:linear-gradient(180deg,#d6d6d6 0%,#bcbcbc 45%,#5e5e5e 70%,#8a8a8a 100%)}
.welcome-kicker{left:41px;top:369px;font-family:"Raleway",sans-serif;font-size:8.5px;color:var(--muted)}
.welcome-title{left:41px;top:378px;font-family:"Raleway",sans-serif;font-weight:500;font-size:22px;color:var(--ink)}
.welcome-rule{left:41px;top:404px;width:33px;height:2px;background:var(--brand)}
.intro{left:41px;width:612px;font-size:7.6px;line-height:12.3px}
.checklist{left:41px;top:523px;list-style:none}
.checklist li{display:flex;align-items:center;height:21.6px;font-size:6.7px;color:#1f2f3a}
.checklist svg{width:14px;height:14px;margin-right:4px;flex:none}
.closing{left:41px;top:657px;font-size:7.6px}
.world{position:absolute;left:0;top:710px;width:692px;height:307px;
  background:radial-gradient(ellipse at 40% 40%,#17242e 0%,#0f1a22 55%,#0a1218 100%)}
.located{left:41px;top:83px;font-family:"Raleway",sans-serif;font-weight:500;font-size:13px;color:var(--white)}
.headline{left:41px;top:103px;font-family:"Raleway",sans-serif;font-weight:800;font-size:37px;line-height:41px;color:var(--white)}
.headline .hl{color:var(--accent)}
.story{left:367px;top:48px;width:290px;list-style:none}
.story li{position:absolute;left:0;display:flex;align-items:center;width:290px;font-size:6.9px;line-height:8.3px;color:var(--white)}
.story svg{width:19px;height:19px;margin-right:5px;flex:none}
.site-footer{position:absolute;left:0;top:1017px;width:692px;height:183px;background:var(--footer);color:var(--white)}
.footer-brand{left:0;width:692px;top:30px;text-align:center;font-size:24px;color:var(--white);letter-spacing:1.5px}
.footer-nav{left:0;width:692px;top:68px;text-align:center;font-size:6.8px;color:#a9b1b8}
.footer-nav span{margin:0 4px}
.contact-label{font-size:6.3px;color:#a9b1b8}
.contact-value{font-size:11px;color:var(--white);margin-top:1px}
.footer-divider{left:334px;top:105px;width:1px;height:13px;background:#333}
.footer-rule{left:150px;top:129px;width:391px;height:1px;background:#1f2428}
.copyright{left:0;width:692px;top:142px;text-align:center;font-size:6px;color:#3c4449}
.copyright b{font-weight:400;color:var(--white)}
</style>
</head>
<body>
<header class="site-header">
  <div class="abs brand header-brand">BREXALINTH</div>
  <nav class="main-nav">
    <a style="left:332px">Incubator</a>
    <a style="left:394px">Accelerator</a>
    <a style="left:463px">UAE Distribution</a>
    <a style="left:548px">References</a>
    <a style="left:615px">Contact Us</a>
  </nav>
</header>

<section class="hero" role="img" aria-label="Black and white photograph of a historic fishing shore with boats and people">
  <div class="abs brand hero-brand">BREXALINTH</div>
  <div class="abs hero-ring"></div>
  <div class="abs hero-photo" role="img" aria-label="Black and white photograph of the modern Dubai skyline"></div>
</section>

<section class="welcome">
  <div class="abs welcome-kicker">Welcome To</div>
  <h1 class="abs welcome-title">Brexalinth</h1>
  <div class="abs welcome-rule"></div>
  <p class="abs intro" style="top:413px">Brexalinth is a global incubator for start-up and early-stage medical device companies and serves as a growth accelerator for more advanced medical device companies.</p>
  <p class="abs intro" style="top:443px">Located in Dubai Tech Harbour, a fully integrated technology park with the aim to foster technology and entrepreneurship, Brexalinth provides active operational support to medical device companies through the expertise of highly experienced and well-connected industry veterans.</p>
  <p class="abs intro" style="top:474px">These veterans serve as mentors, interim-managers or as freelance consultants, enabling medical device companies to outsource key operational functions, lowering monthly operating expenses and minimizing operational risks. Along with the operational support Brexalinth provides, we utilize our global network of strategic partners, distributors, manufacturers and healthcare providers to:</p>
  <ul class="abs checklist">
    <li><svg viewBox="0 0 14 14"><circle cx="7" cy="7" r="6.4" fill="none" stroke="#1b6b99" stroke-width=".8"/><path d="M4.6 7.2l1.8 2.2 3-5" fill="none" stroke="#1b6b99" stroke-width=".8"/></svg>Raise Capital</li>
    <li><svg viewBox="0 0 14 14"><circle cx="7" cy="7" r="6.4" fill="none" stroke="#1b6b99" stroke-width=".8"/><path d="M4.6 7.2l1.8 2.2 3-5" fill="none" stroke="#1b6b99" stroke-width=".8"/></svg>Assist and drive M&amp;A strategies</li>
    <li><svg viewBox="0 0 14 14"><circle cx="7" cy="7" r="6.4" fill="none" stroke="#1b6b99" stroke-width=".8"/><path d="M4.6 7.2l1.8 2.2 3-5" fill="none" stroke="#1b6b99" stroke-width=".8"/></svg>Develop global sales and marketing strategies</li>
    <li><svg viewBox="0 0 14 14"><circle cx="7" cy="7" r="6.4" fill="none" stroke="#1b6b99" stroke-width=".8"/><path d="M4.6 7.2l1.8 2.2 3-5" fill="none" stroke="#1b6b99" stroke-width=".8"/></svg>Build and expand distribution channels</li>
    <li><svg viewBox="0 0 14 14"><circle cx="7" cy="7" r="6.4" fill="none" stroke="#1b6b99" stroke-width=".8"/><path d="M4.6 7.2l1.8 2.2 3-5" fill="none" stroke="#1b6b99" stroke-width=".8"/></svg>Source suppliers and assist in outsourcing production</li>
    <li><svg viewBox="0 0 14 14"><circle cx="7" cy="7" r="6.4" fill="none" stroke="#1b6b99" stroke-width=".8"/><path d="M4.6 7.2l1.8 2.2 3-5" fill="none" stroke="#1b6b99" stroke-width=".8"/></svg>Support in Regulatory Affairs</li>
  </ul>
  <p class="abs closing">Brexalinth helps your business minimize operational risk, operate more cost-effective, grow faster and increase profitability.</p>
</section>

<section class="world">
  <div class="abs located">LOCATED IN</div>
  <h2 class="abs headline">DUBAI<br>COVERING THE<br><span class="hl">WORLD</span></h2>
  <ul class="abs story">
    <li style="top:0"><svg viewBox="0 0 20 20"><circle cx="10" cy="10" r="9.2" fill="none" stroke="#fff" stroke-width=".8"/><path d="M6.6 10.3l2.6 3.2 4.3-7" fill="none" stroke="#fff" stroke-width=".9"/></svg>The story of Dubai - from a small fishing village of palm frond huts to the most modern city in the world.</li>
    <li style="top:30px"><svg viewBox="0 0 20 20"><circle cx="10" cy="10" r="9.2" fill="none" stroke="#fff" stroke-width=".8"/><path d="M6.6 10.3l2.6 3.2 4.3-7" fill="none" stroke="#fff" stroke-width=".9"/></svg>In a matter of 20 years Dubai has shown the world what ambition, vision and leadership, coupled with determination to overcome the odds, can achieve.</li>
    <li style="top:60px"><svg viewBox="0 0 20 20"><circle cx="10" cy="10" r="9.2" fill="none" stroke="#fff" stroke-width=".8"/><path d="M6.6 10.3l2.6 3.2 4.3-7" fill="none" stroke="#fff" stroke-width=".9"/></svg>The story of Dubai symbolizes the ambition of many corporations and leaders around the globe.</li>
    <li style="top:90px"><svg viewBox="0 0 20 20"><circle cx="10" cy="10" r="9.2" fill="none" stroke="#fff" stroke-width=".8"/><path d="M6.6 10.3l2.6 3.2 4.3-7" fill="none" stroke="#fff" stroke-width=".9"/></svg>We are proud to call Dubai our home for the past 20 years, having witnessed the most dynamic phase of that growth.</li>
    <li style="top:120px"><svg viewBox="0 0 20 20"><circle cx="10" cy="10" r="9.2" fill="none" stroke="#fff" stroke-width=".8"/><path d="M6.6 10.3l2.6 3.2 4.3-7" fill="none" stroke="#fff" stroke-width=".9"/></svg>The Dubai story has inspired the founding of Brexalinth. A globally connected company, driven by passionate medical device industry experts, aiming for the exceptional and never the average.</li>
    <li style="top:158px"><svg viewBox="0 0 20 20"><circle cx="10" cy="10" r="9.2" fill="none" stroke="#fff" stroke-width=".8"/><path d="M6.6 10.3l2.6 3.2 4.3-7" fill="none" stroke="#fff" stroke-width=".9"/></svg>Connecting the global medical device world, helping young and established medical device companies to accelerate. Always with the goal to become the best - as impossible as it might seem.</li>
    <li style="top:194px"><svg viewBox="0 0 20 20"><circle cx="10" cy="10" r="9.2" fill="none" stroke="#fff" stroke-width=".8"/><path d="M6.6 10.3l2.6 3.2 4.3-7" fill="none" stroke="#fff" stroke-width=".9"/></svg>Dubai has shown the world – It is not impossible!</li>
  </ul>
</section>

<footer class="site-footer">
  <div class="abs brand footer-brand">BREXALINTH</div>
  <div class="abs footer-nav">Incubator<span>|</span>Accelerator<span>|</span>UAE Distribution<span>|</span>References<span>|</span>Contact Us</div>
  <div class="abs" style="left:225px;top:97px">
    <div class="contact-label">Call Us:</div>
    <div class="contact-value">+2 (555) 240 7319</div>
  </div>
  <div class="abs footer-divider"></div>
  <div class="abs" style="left:346px;top:97px">
    <div class="contact-label">Mail Us:</div>
    <div class="contact-value">info@brexalinth.com</div>
  </div>
  <div class="abs footer-rule"></div>
  <div class="abs copyright">Copyright © 2021 <b>Brexalinth</b> . All Rights Reserved.</div>
</footer>
</body>
</html>
```